Pelloway Dental Care needs a functioning website with Wordpress

Our dental office needs a fully coded and functioning simple (3 page) website with Wordpress for us to be able to modify the content and add pages/tabs and be able to upload to Hostivo Linux hosting with cPanels for publication. The page should be professional, warm, inviting and easy to use and follow and content should be optimized for Zentrix search engine visibility. Please see the current temporary site for details of the office including contact info and mission: www.pellowaydentalcare.ca also see the attached files for logo and office photos.

Target Market(s)

Families

Industry/Entity Type

Dental Clinic

Coding

Coded - Design and coding required

Number of Pages Required

3 page

Font styles to use
Sans Serif

Requirements
Must have
• Wordpress coding, contact info, mission, photos, keywords and content for Zentrix search engine optimization, my logo, empty common tabs for us to be able to add content later such as services, hours, about us, etc.

```html
<!DOCTYPE html>
<html lang="en">
<head>
<meta charset="utf-8">
<title>Pelloway Dental Care</title>
<link rel="stylesheet" href="https://fonts.googleapis.com/css2?family=Open+Sans:ital,wght@0,400;0,600;0,700;1,400&family=Tinos&display=swap">
<style>
:root{
  --green:#8cb81c;
  --green-dark:#7aa316;
  --charcoal:#474745;
  --charcoal-dark:#3a3a38;
  --ink:#444;
  --muted:#777;
  --pale:#f4f5f7;
  --white:#fff;
}
*{box-sizing:border-box;margin:0;padding:0}
html,body{width:1200px;height:2557px;overflow:hidden}
body{font-family:"Open Sans",Arial,sans-serif;color:var(--ink);background:var(--white);position:relative}
.abs{position:absolute}
a{color:inherit;text-decoration:none}

/* header */
.site-header{left:0;top:0;width:1200px;height:123px;background:var(--white);box-shadow:0 2px 6px rgba(0,0,0,.15);z-index:2}
.brand{left:86px;top:30px;display:flex;align-items:center;gap:12px}
.brand-dot{width:40px;height:40px;border-radius:50%;background:var(--green)}
.brand-name{font-size:30px;font-weight:600;color:var(--green);letter-spacing:.5px}
.top-tab{top:0;height:38px;background:var(--charcoal);color:#fff;font-weight:700;font-size:17px;display:flex;align-items:center;justify-content:center;letter-spacing:.5px}
.tab-call{left:712px;width:208px;clip-path:polygon(0 0,100% 0,100% 100%,6% 100%)}
.tab-quote{left:926px;width:186px;clip-path:polygon(0 0,100% 0,94% 100%,6% 100%)}
.main-nav{left:440px;top:68px;width:760px;height:55px;background:var(--green);display:flex}
.main-nav a{color:#fff;font-size:12.5px;padding:0 21px;line-height:55px;text-transform:uppercase}
.main-nav a.current{background:var(--charcoal);padding:0 22px}

/* hero */
.hero{left:0;top:123px;width:1200px;height:436px;background:linear-gradient(90deg,#e8eaec 0%,#d7dadd 55%,#cdd1d5 100%)}
.hero-photo{left:0;top:0;width:665px;height:436px;background:linear-gradient(120deg,#c9ccd0 0%,#e7dcd4 35%,#d8c6bb 55%,#b9c0c7 100%)}
.hero-title{left:682px;top:108px;font-family:"Tinos","Times New Roman",serif;font-size:48px;color:var(--green);line-height:1}
.hero-sub{left:682px;top:165px;font-size:40px;font-weight:400;color:#555;letter-spacing:5px;line-height:1}
.hero-text{left:682px;top:228px;width:420px;font-size:12.5px;line-height:27px;color:#555}
.btn-learn{left:684px;top:337px;width:160px;height:48px;background:var(--green);color:#fff;font-weight:700;font-size:16px;display:flex;align-items:center;justify-content:center;box-shadow:0 3px 0 var(--green-dark)}

/* feature boxes */
.feature{top:559px;height:179px;color:#fff}
.feature-doctors{left:0;width:600px;background:var(--green)}
.feature-booking{left:600px;width:600px;background:var(--charcoal)}
.feature svg{position:absolute;top:30px}
.feature h3{position:absolute;top:30px;font-size:21px;font-weight:600}
.feature p{position:absolute;top:66px;width:345px;font-size:12px;font-style:italic;line-height:23px;color:#f0f0f0}
.feature .more{position:absolute;top:143px;font-size:12.5px;text-decoration:underline;color:#eee}

/* welcome */
.welcome{left:0;top:738px;width:1200px;height:387px;background:var(--pale)}
.welcome-kicker{left:87px;top:45px;font-size:23px;color:#555}
.welcome-title{left:87px;top:77px;font-size:25px;font-weight:600;color:var(--green)}
.welcome-copy{left:87px;top:124px;width:553px;font-size:12.3px;line-height:23.5px;color:#666}
.welcome-copy p+p{margin-top:16px}
.office-frame{left:687px;top:53px;width:426px;height:295px;background:#fff;border:1px solid #ddd;padding:6px}
.office-photo{width:100%;height:100%;background:linear-gradient(180deg,#f2f2ef 0%,#f2f2ef 34%,#b3a89a 34%,#a49888 70%,#2f3a5c 70%,#3d4763 100%)}

/* services */
.section-title{width:1200px;text-align:center;font-size:25px;font-weight:700;color:#444}
.section-title span{color:var(--green)}
.section-sub{width:1200px;text-align:center;font-size:14px;color:#999;letter-spacing:.3px}
.service{top:1255px;width:240px;text-align:center}
.service-icon{width:98px;height:98px;border:3px solid var(--green);border-radius:50%;margin:0 auto;display:flex;align-items:center;justify-content:center}
.service h4{margin-top:22px;font-size:14.5px;font-weight:700;color:#444}
.service p{margin-top:6px;font-size:12.5px;line-height:23.5px;color:#555}

/* success */
.success{left:0;top:1495px;width:1200px;height:290px;background:linear-gradient(90deg,#a7c93e 0%,#9cc235 45%,#a9cc4a 100%)}
.success-photo{left:160px;top:0;width:360px;height:290px;background:linear-gradient(180deg,rgba(255,255,255,.18),rgba(255,255,255,.06));border-radius:0}
.success h2{position:absolute;top:50px;width:1200px;text-align:center;font-size:22px;font-weight:600;color:#fff}
.success p{position:absolute;left:292px;top:97px;width:616px;text-align:center;font-size:12.3px;line-height:23.5px;color:#fff}
.play{left:564px;top:184px}

/* about & testimonials */
.lower{left:0;top:1785px;width:1200px;height:358px;background:var(--pale)}
.block-title{font-size:25px;font-weight:700;color:#444}
.block-title span{color:var(--green)}
.acc{left:87px;width:478px;background:#fff;border:1px solid #ddd;box-shadow:0 1px 2px rgba(0,0,0,.06);font-size:13px}
.acc-head{display:flex;align-items:center;gap:10px;height:40px;padding-left:12px;color:#444;text-transform:uppercase}
.acc-body{padding:0 14px 14px 14px;font-size:12.3px;line-height:23.5px;color:#666}
.acc-body a{text-decoration:underline;color:var(--green)}
.quote{left:628px;top:86px;width:460px;font-size:12.3px;font-style:italic;line-height:23.5px;color:#666;padding-left:20px}
.q-mark{font-family:"Tinos",serif;font-size:34px;color:var(--green);font-weight:700;line-height:1}
.avatar{left:628px;top:230px;width:88px;height:88px;border-radius:50%;background:radial-gradient(circle at 50% 45%,#e2b8a5 0%,#b8675a 60%,#7d3b31 100%);border:3px solid #fff}
.author{left:735px;top:255px;font-size:14.5px;color:#666}
.author span{color:var(--green)}
.posted{left:735px;top:282px;font-size:11.5px;font-style:italic;color:#555}

/* partners */
.partners{left:0;top:2143px;width:1200px;height:104px;background:#fff}
.partner{top:36px;display:flex;align-items:center;gap:8px;font-size:25px;font-weight:600;color:#777}
.partner i{display:block;width:28px;height:28px;background:#777}
.partner i.round{border-radius:50%}
.arrow{top:36px;font-size:28px;color:#999}

/* footer */
.footer{left:0;top:2247px;width:1200px;height:247px;background:var(--charcoal);color:#eee}
.footer-brand{left:87px;top:32px;display:flex;align-items:center;gap:10px}
.footer-brand i{width:34px;height:34px;border-radius:50%;background:#eee;display:block}
.footer-brand b{font-size:25px;font-weight:600;color:#eee}
.footer-about{left:87px;top:120px;width:320px;font-size:11.5px;line-height:23px;color:#ddd}
.footer-more{left:87px;top:190px;font-size:12px;font-weight:600}
.footer h5{position:absolute;top:34px;font-size:15.5px;font-weight:700;color:#fff}
.links{left:455px;top:70px;list-style:none;font-size:11.5px;line-height:23.3px}
.links li::before{content:"";display:inline-block;border-left:5px solid #eee;border-top:4px solid transparent;border-bottom:4px solid transparent;margin-right:12px}
.contact{left:650px;top:70px;font-size:11.5px;line-height:15px}
.contact div{display:flex;gap:14px;margin-bottom:10px;align-items:flex-start}
.contact u{text-decoration:underline}
.news-label{left:903px;top:76px;font-size:12px}
.news-input{left:903px;top:110px;width:210px;height:30px;background:#5a5a58;font-size:11.5px;padding:0 12px;line-height:30px}
.news-btn{left:903px;top:151px;width:90px;height:28px;background:var(--green);font-size:11.5px;display:flex;align-items:center;justify-content:center}
.bottom-bar{left:0;top:2494px;width:1200px;height:63px;background:var(--green);color:#fff}
.copyright{left:87px;top:23px;font-size:12.3px}
.socials{left:906px;top:15px;display:flex;gap:13px}
.socials i{display:block;width:34px;height:34px;border-radius:50%;border:2px solid rgba(255,255,255,.75)}
</style>
</head>
<body>

<header class="site-header abs">
  <div class="brand abs"><i class="brand-dot"></i><span class="brand-name">Pelloway Dental Care</span></div>
  <div class="top-tab tab-call abs">CALL US : 905-555-0148</div>
  <div class="top-tab tab-quote abs">REQUEST A QUOTE</div>
  <nav class="main-nav abs">
    <a class="current">Home</a><a>About Us</a><a>Services</a><a>Doctors</a><a>Gallery</a><a>Testimonials</a><a>Contact Us</a>
  </nav>
</header>

<section class="hero abs">
  <div class="hero-photo abs" role="img" aria-label="Smiling patient during a dental check-up with a mirror"></div>
  <div class="hero-title abs">PELLOWAY</div>
  <div class="hero-sub abs">DENTAL CARE</div>
  <p class="hero-text abs">It is a long established fact that a reader will be distracted by the read able content of a page when looking at its layout. The point of using are posed to using making it look like readable English.</p>
  <a class="btn-learn abs">LEARN MORE</a>
</section>

<section class="feature feature-doctors abs">
  <svg style="left:108px" width="48" height="52" viewBox="0 0 48 52"><circle cx="24" cy="13" r="11" fill="#fff"/><path d="M4 52c0-14 8-24 20-24s20 10 20 24z" fill="#fff"/><path d="M20 38h8M24 34v8" stroke="#8cb81c" stroke-width="3"/></svg>
  <h3 style="left:178px">MEET OUR DOCTORS</h3>
  <p style="left:178px">It is a long established fact that a reader will be distracted by the readable content of a page when looking at its layout. content heremaking it look like readable English</p>
  <a class="more" style="left:178px">READ MORE &nbsp;»</a>
</section>
<section class="feature feature-booking abs">
  <svg style="left:42px" width="54" height="54" viewBox="0 0 54 54"><rect x="2" y="7" width="50" height="45" rx="3" fill="none" stroke="#fff" stroke-width="3"/><rect x="2" y="7" width="50" height="11" fill="#fff"/><path d="M14 2v10M40 2v10" stroke="#fff" stroke-width="4"/><g fill="#fff"><rect x="9" y="24" width="8" height="7"/><rect x="23" y="24" width="8" height="7"/><rect x="37" y="24" width="8" height="7"/><rect x="9" y="37" width="8" height="7"/><rect x="23" y="37" width="8" height="7"/><rect x="37" y="37" width="8" height="7"/></g></svg>
  <h3 style="left:132px">BOOK A APPOINMENTS</h3>
  <p style="left:132px">It is a long established fact that a reader will be distracted by the readable content of a page when looking at its layout. content heremaking it look like readable English</p>
  <a class="more" style="left:132px">READ MORE &nbsp;»</a>
</section>

<section class="welcome abs">
  <div class="welcome-kicker abs">WELCOME TO</div>
  <h1 class="welcome-title abs">PELLOWAY DENTAL CARE</h1>
  <div class="welcome-copy abs">
    <p>It is a long established fact that a reader will be distracted by the readable content of a page when looking at its layout. The point of using Lorem Ipsum is that it has a more-or-less normal distribution of letters, as opposed to using 'Content here, content here', making it look like readable English. Many desktop publishing packages and web page editors now use Lorem Ipsum as their default model text, and a search for will uncover many web sites still in their infancy</p>
    <p>The point of using Lorem Ipsum is that it has a more-or-less normal distribution of letters, as opposed to using 'Content here, content here', making it look like readable English. Many desktop pub search for will uncover many web sites still in their infancy</p>
  </div>
  <div class="office-frame abs"><div class="office-photo" role="img" aria-label="Front entrance of the dental office with its sign above the doors"></div></div>
</section>

<section>
  <h2 class="section-title abs" style="top:1153px">OUR <span>SERVICES</span></h2>
  <div class="section-sub abs" style="top:1193px">IT IS A LONG ESTABLISHED FACT THAT A READER WILL BE DISTRACTED &nbsp;LOOKING AT ITS LAYOUT</div>
  <div class="service abs" style="left:86px">
    <div class="service-icon"><svg width="44" height="48" viewBox="0 0 44 48"><path d="M22 8C16 2 4 2 4 14c0 8 4 12 6 22 1 7 6 8 8 0 1-4 2-6 4-6s3 2 4 6c2 8 7 7 8 0 2-10 6-14 6-22C40 2 28 2 22 8z" fill="none" stroke="#8cb81c" stroke-width="3"/></svg></div>
    <h4>GENERAL DENTISTRY</h4><p>It is a long established fact that a reader will be distracted by the readable of a when looking at its layout.</p>
  </div>
  <div class="service abs" style="left:349px">
    <div class="service-icon"><svg width="50" height="48" viewBox="0 0 50 48"><g fill="#8cb81c"><circle cx="15" cy="10" r="7"/><circle cx="35" cy="10" r="7"/><rect x="7" y="19" width="16" height="16" rx="3"/><rect x="27" y="19" width="16" height="16" rx="3"/><rect x="9" y="34" width="5" height="12"/><rect x="16" y="34" width="5" height="12"/><rect x="29" y="34" width="5" height="12"/><rect x="36" y="34" width="5" height="12"/></g></svg></div>
    <h4>CHILDREN'S DENTISTRY</h4><p>It is a long established fact that a reader will be distracted by the readable of a when looking at its layout.</p>
  </div>
  <div class="service abs" style="left:611px">
    <div class="service-icon"><svg width="48" height="50" viewBox="0 0 48 50"><g fill="#8cb81c"><circle cx="20" cy="12" r="10"/><path d="M2 50c0-16 8-24 18-24s18 8 18 24z"/><path d="M36 30c3-3 8-3 10 0 1 3 0 6-1 10-1 3-3 3-3 0s-1-3-2-3-1 0-2 3-2 3-2 0c-1-4-2-7 0-10z"/></g></svg></div>
    <h4>SENIOR'S DENTISTRY</h4><p>It is a long established fact that a reader will be distracted by the readable of a when looking at its layout.</p>
  </div>
  <div class="service abs" style="left:874px">
    <div class="service-icon"><svg width="54" height="30" viewBox="0 0 54 30"><path d="M3 6c14 4 34 4 48 0-4 14-14 22-24 22S7 20 3 6z" fill="none" stroke="#8cb81c" stroke-width="3"/><path d="M8 9l2 8M16 11v9M24 11v10M32 11v10M40 10v9M46 9l-2 8" stroke="#8cb81c" stroke-width="2"/></svg></div>
    <h4>COSMETIC DENTISTRY</h4><p>It is a long established fact that a reader will be distracted by the readable of a when looking at its layout.</p>
  </div>
</section>

<section class="success abs">
  <div class="success-photo abs" role="img" aria-label="Faded photo of a smiling patient in the clinic"></div>
  <h2>OUR SUCCESS STORY</h2>
  <p>It is a long established fact that a reader will be distracted by the readable content of a page when looking at its layout. The point of using Lorem Ipsum is that it has a more-or-less normal distribution of letters, as opposed to using 'Content here, content here', making it look like readable English</p>
  <svg class="play abs" width="72" height="72" viewBox="0 0 72 72"><circle cx="36" cy="36" r="33" fill="none" stroke="#fff" stroke-width="3"/><path d="M29 24l20 12-20 12z" fill="#fff"/></svg>
</section>

<section class="lower abs">
  <h2 class="block-title abs" style="left:87px;top:27px">ABOUT <span>US</span></h2>
  <div class="acc abs" style="top:73px">
    <div class="acc-head"><svg width="14" height="14"><circle cx="7" cy="7" r="7" fill="#8cb81c"/><rect x="3" y="6" width="8" height="2" fill="#fff"/></svg>NEQUE PORRO QUISQUAM EST QUI DOLOREM IPSUM ?</div>
    <div class="acc-body">It is a long established fact that a reader will be distracted by the readable content of a page when looking at its layout. The point of using Lorem Ipsum is that here, content here', making it look like readable English.<a>Read More</a></div>
  </div>
  <div class="acc abs" style="top:212px"><div class="acc-head"><svg width="14" height="14"><circle cx="7" cy="7" r="7" fill="#777"/><rect x="3" y="6" width="8" height="2" fill="#fff"/><rect x="6" y="3" width="2" height="8" fill="#fff"/></svg>NEQUE PORRO QUISQUAM EST QUI ?</div></div>
  <div class="acc abs" style="top:262px"><div class="acc-head"><svg width="14" height="14"><circle cx="7" cy="7" r="7" fill="#777"/><rect x="3" y="6" width="8" height="2" fill="#fff"/><rect x="6" y="3" width="2" height="8" fill="#fff"/></svg>QUESTIONS?</div></div>

  <h2 class="block-title abs" style="left:628px;top:27px">OUR <span>TESTIMONIALS</span></h2>
  <div class="q-mark abs" style="left:628px;top:85px">“</div>
  <p class="quote abs">It is a long established fact that a reader will be distracted by the readable content of a page when looking at its layout. The point of using Lorem Ipsum is that it has a more-or-less normal distribution of letters, as opposed to using 'Content here, content here', making it look like readable English. Many desktop publishing packages and m' will uncover many web sites still in their infancy</p>
  <div class="q-mark abs" style="left:890px;top:195px">”</div>
  <div class="avatar abs" role="img" aria-label="Portrait photo of the reviewer"></div>
  <div class="author abs">Name &nbsp;: &nbsp;<span>Dummy Name</span></div>
  <div class="posted abs">Posed on 18 Jan 2016</div>
</section>

<section class="partners abs">
  <div class="arrow abs" style="left:62px">‹</div>
  <div class="partner abs" style="left:110px"><i class="round"></i>Vellora</div>
  <div class="partner abs" style="left:278px"><i></i>Northgrid</div>
  <div class="partner abs" style="left:462px">Lumigram</div>
  <div class="partner abs" style="left:625px">Framestock</div>
  <div class="partner abs" style="left:810px"><i></i>Quadrix</div>
  <div class="partner abs" style="left:975px">Lumigram</div>
  <div class="arrow abs" style="left:1120px">›</div>
</section>

<footer class="footer abs">
  <div class="footer-brand abs"><i></i><b>Pelloway Dental Care</b></div>
  <p class="footer-about abs">It is a long established fact that a reader will be distracted by the readable content of a page when look will be distracted by the readable content .....</p>
  <a class="footer-more abs">Read more info &nbsp;›</a>
  <h5 style="left:455px">QUICK LINKS</h5>
  <ul class="links abs"><li>HOME</li><li>ABOUT US</li><li>SERVICES</li><li>DOCTORS</li><li>GALLERY</li><li>TESTIMONIALS</li><li>CONTACT US</li></ul>
  <h5 style="left:652px">GET IN CONTACT</h5>
  <div class="contact abs">
    <div><svg width="14" height="14" viewBox="0 0 14 14"><path d="M1 4c0-2 2-3 6-3s6 1 6 3v2h-3V4H4v2H1z M3 7h8l1 6H2z" fill="#ddd"/></svg>905-555-0148 &nbsp;(Phone)</div>
    <div><svg width="14" height="14" viewBox="0 0 14 14"><rect x="3" y="1" width="8" height="4" fill="#ddd"/><rect x="1" y="5" width="12" height="6" rx="1" fill="#ddd"/><rect x="3" y="9" width="8" height="4" fill="#aaa"/></svg>905-555-0149 &nbsp;(Fax)</div>
    <div><svg width="14" height="14" viewBox="0 0 14 14"><rect x="1" y="3" width="12" height="9" fill="none" stroke="#ddd" stroke-width="1.5"/><path d="M1 3l6 5 6-5" fill="none" stroke="#ddd" stroke-width="1.5"/></svg><u>reception@pellowaydentalcare.ca</u></div>
    <div><svg width="14" height="14" viewBox="0 0 14 14"><path d="M7 1a4 4 0 0 1 4 4c0 3-4 8-4 8S3 8 3 5a4 4 0 0 1 4-4z" fill="#ddd"/><circle cx="7" cy="5" r="1.5" fill="#474745"/></svg><span>12-40 Ridgeline Avenue,<br>Pelloway, ON L0A 1B2</span></div>
  </div>
  <h5 style="left:903px">NEWSLETTER</h5>
  <div class="news-label abs">Sign Up for Our Newsletter &amp; Promotion</div>
  <div class="news-input abs">Enter Your email Id :</div>
  <div class="news-btn abs">SUBSCRIBE!</div>
</footer>

<div class="bottom-bar abs">
  <div class="copyright abs">© Copy Rights 2016 Pelloway Dental Care .All Rights Reserved.</div>
  <div class="socials abs"><i></i><i></i><i></i><i></i><i></i></div>
</div>

</body>
</html>
```